Stationery Design Project

I would like professional stationery that will be branded with our logo.

also, I have application- multipage that I would like to brand. I will attach an example of one of the pages.

Perhaps- this could be the same design, but due to spacing, it may be best to do slight variations.

Target Market(s)

The audience is our donors and supporters who have a heart for the disenfranchised. They are mostly professional and often have significant wealth. They do their work with excellence and I want an image that makes them feel confident we know what we are doing. this is why i tend to say i want a professional look. Also, I want the feel to be uplifting, something that is somewhat artistic and classy.

Industry/Entity Type

It Professional

Font styles to use
Serif

Requirements
Must have
• Generally, simple but I do want a stylized look...

512-684-2730
www.brightmorrowfund.org
PO Box 384927 Dallas, TX 75211
admin@brightmorrowfund.org
Nice to have
• i like to use the colors in our logo
Should not have
• hearts and country look

```html
<!DOCTYPE html>
<html lang="en">
<head>
<meta charset="utf-8">
<title>Bright Morrow Fund Stationery</title>
<link rel="stylesheet" href="https://fonts.googleapis.com/css2?family=Cinzel:wght@500&family=Cormorant+Garamond:ital,wght@0,500;0,600;1,500&display=swap">
<style>
  :root {
    --backdrop: #a3a3a4;
    --paper: #ffffff;
    --charcoal: #3c3c3d;
    --charcoal-edge: #2f2f30;
    --brand-blue: #1d87e0;
    --ink: #4a4a4a;
    --ink-soft: #8a8a8a;
    --faint: rgba(0, 0, 0, 0.035);
    --faint-dark: rgba(255, 255, 255, 0.04);
  }
  * { box-sizing: border-box; margin: 0; padding: 0; }
  html, body { width: 1200px; height: 945px; overflow: hidden; }
  body {
    position: relative;
    background: var(--backdrop);
    font-family: "Cormorant Garamond", Georgia, serif;
    color: var(--ink);
  }
  .piece {
    position: absolute;
    background: var(--paper);
    box-shadow: 0 2px 6px rgba(0, 0, 0, 0.18);
    overflow: hidden;
  }
  .piece--dark { background: var(--charcoal); color: #ececec; }

  .brand { display: flex; align-items: center; gap: 7px; }
  .brand__dot { border-radius: 50%; background: var(--brand-blue); flex: none; }
  .brand__name {
    font-family: "Cinzel", "Times New Roman", serif;
    font-weight: 500;
    letter-spacing: 0.02em;
    white-space: nowrap;
    color: var(--ink);
  }
  .piece--dark .brand__name { color: #f2f2f2; }
  .brand__tagline { font-style: italic; color: var(--ink-soft); white-space: nowrap; }
  .piece--dark .brand__tagline { color: #c9c9c9; }

  .emblem-ghost { position: absolute; border-radius: 50%; background: var(--faint); }
  .piece--dark .emblem-ghost { background: var(--faint-dark); }

  /* Letterhead */
  .letterhead { left: 250px; top: 40px; width: 360px; height: 510px; }
  .letterhead .brand-block { position: absolute; top: 34px; left: 0; right: 0; display: flex; flex-direction: column; align-items: center; }
  .letterhead .brand__dot { width: 22px; height: 22px; }
  .letterhead .brand__name { font-size: 15px; }
  .letterhead .brand__tagline { font-size: 9px; margin-left: 60px; }
  .letterhead .emblem-ghost { width: 220px; height: 220px; left: 70px; top: 150px; }
  .letterhead__footer { position: absolute; left: 30px; right: 30px; bottom: 34px; border-top: 1px solid #9a9a9a; padding-top: 6px; font-size: 8px; line-height: 1.5; text-align: center; color: var(--ink-soft); }
  .label { color: var(--brand-blue); font-weight: 600; }

  /* Folder */
  .folder { left: 660px; top: 40px; width: 380px; height: 520px; }
  .folder__spine { position: absolute; left: 0; top: 0; bottom: 0; width: 14px; background: var(--charcoal-edge); border-right: 1px solid #4a4a4b; }
  .folder .brand-block { position: absolute; top: 70px; right: 34px; display: flex; flex-direction: column; align-items: flex-end; }
  .folder .brand__dot { width: 30px; height: 30px; }
  .folder .brand__name { font-size: 22px; }
  .folder .brand__tagline { font-size: 12px; }
  .folder .emblem-ghost { width: 260px; height: 260px; left: 70px; top: 210px; }

  /* Business cards */
  .card { left: 40px; width: 180px; height: 104px; }
  .card--front { top: 150px; }
  .card--back { top: 280px; display: flex; align-items: center; justify-content: center; }
  .card .brand__dot { width: 14px; height: 14px; }
  .card .brand__name { font-size: 11px; }
  .card--front .brand { position: absolute; left: 12px; top: 14px; }
  .card__holder { position: absolute; right: 12px; top: 46px; text-align: right; }
  .card__name { font-family: "Cinzel", serif; font-size: 8px; color: var(--brand-blue); }
  .card__role { font-size: 7px; font-style: italic; color: var(--ink-soft); }
  .card__contact { position: absolute; left: 12px; bottom: 10px; font-size: 6.5px; line-height: 1.45; color: var(--ink-soft); }

  /* Envelopes */
  .envelope { top: 610px; width: 430px; height: 215px; }
  .envelope--front { left: 180px; }
  .envelope--front .brand-block { position: absolute; left: 28px; top: 22px; display: flex; flex-direction: column; align-items: flex-start; }
  .envelope--front .brand__dot { width: 18px; height: 18px; }
  .envelope--front .brand__name { font-size: 13px; }
  .envelope--front .brand__tagline { font-size: 8px; margin-left: 25px; }
  .envelope--front .emblem-ghost { width: 150px; height: 150px; left: 220px; top: 40px; }
  .envelope__return { position: absolute; left: 28px; bottom: 24px; font-size: 8px; color: var(--ink-soft); }
  .envelope--back { left: 640px; }
  .envelope__flap { position: absolute; left: 0; top: 0; width: 430px; height: 95px; }
  .envelope--back .brand__dot { position: absolute; width: 24px; height: 24px; left: 203px; top: 34px; }
</style>
</head>
<body>

  <section class="piece card card--front" aria-label="Business card, front">
    <div class="brand"><span class="brand__dot"></span><span class="brand__name">Bright Morrow Fund</span></div>
    <div class="card__holder">
      <div class="card__name">Daniel Hollis</div>
      <div class="card__role">Director</div>
    </div>
    <div class="card__contact">
      <span class="label">Tel:</span> 512-684-2730<br>
      <span class="label">Web:</span> www.brightmorrowfund.org<br>
      <span class="label">Email:</span> admin@brightmorrowfund.org
    </div>
  </section>

  <section class="piece piece--dark card card--back" aria-label="Business card, back">
    <div class="brand"><span class="brand__dot"></span><span class="brand__name">Bright Morrow Fund</span></div>
  </section>

  <section class="piece letterhead" aria-label="Letterhead">
    <div class="emblem-ghost" role="img" aria-label="Faint brand emblem watermark"></div>
    <div class="brand-block">
      <div class="brand"><span class="brand__dot"></span><span class="brand__name">Bright Morrow Fund</span></div>
      <div class="brand__tagline">Where new hope rises</div>
    </div>
    <div class="letterhead__footer">
      PO Box 384927 Dallas, TX 75211 &nbsp;|&nbsp; <span class="label">Tel:</span> 512-684-2730<br>
      <span class="label">Web:</span> www.brightmorrowfund.org &nbsp;|&nbsp; <span class="label">Email:</span> admin@brightmorrowfund.org
    </div>
  </section>

  <section class="piece piece--dark folder" aria-label="Presentation folder">
    <div class="folder__spine"></div>
    <div class="emblem-ghost" role="img" aria-label="Faint brand emblem watermark"></div>
    <div class="brand-block">
      <div class="brand"><span class="brand__dot"></span><span class="brand__name">Bright Morrow Fund</span></div>
      <div class="brand__tagline">Where new hope rises</div>
    </div>
  </section>

  <section class="piece envelope envelope--front" aria-label="Envelope, front">
    <div class="emblem-ghost" role="img" aria-label="Faint brand emblem watermark"></div>
    <div class="brand-block">
      <div class="brand"><span class="brand__dot"></span><span class="brand__name">Bright Morrow Fund</span></div>
      <div class="brand__tagline">Where new hope rises</div>
    </div>
    <div class="envelope__return">PO Box 384927 Dallas, TX 75211</div>
  </section>

  <section class="piece envelope envelope--back" aria-label="Envelope, back">
    <svg class="envelope__flap" viewBox="0 0 430 95" aria-hidden="true">
      <path d="M0 0 H430 V58 L390 95 H40 L0 58 Z" fill="var(--charcoal)"/>
    </svg>
    <span class="brand__dot"></span>
  </section>

</body>
</html>
```